Pest Control Company needs business card!

Hi there, we need a business card designed for our new Pest Control Company. Ideally this card will be simple, yet feel elegant and high end. We want to use the colours Orange, Black and White. Please see our attached logo for the exact colours.

Business card details:

Phone - 0461 275 804
Name - Gavin Holloway
Email - Info@steadfastverminguard.com.au

We would also like to include the following list with dot points:

SERVICES / INSPECTIONS

Termites, Wood Borers, Ants, Cockroaches, Spiders, Fleas, Mice, Rats, Bed Bugs, & More!

```html
<!DOCTYPE html>
<html lang="en">
<head>
<meta charset="utf-8">
<title>Steadfast Vermin Guard — Business Card</title>
<link href="https://fonts.googleapis.com/css2?family=Roboto:wght@400&family=Roboto+Condensed:wght@700&display=swap" rel="stylesheet">
<style>
  :root {
    --board: #a7a8ab;
    --paper: #ffffff;
    --ink: #231f20;
    --signal: #ed1c24;
  }
  * { margin: 0; padding: 0; box-sizing: border-box; }
  html, body { width: 984px; height: 1200px; overflow: hidden; background: var(--board); }
  .canvas { position: relative; width: 984px; height: 1200px; }
  .shapes { position: absolute; inset: 0; width: 984px; height: 1200px; }

  .wordmark {
    position: absolute;
    font-family: "Roboto Condensed", "Arial Narrow", sans-serif;
    font-weight: 700;
    color: var(--ink);
    text-transform: uppercase;
    line-height: 0.95;
    letter-spacing: -0.5px;
  }
  .wordmark--front { left: 92px; top: 112px; font-size: 54px; }
  .wordmark--back { left: 300px; top: 790px; font-size: 60px; }

  .holder-name {
    position: absolute;
    right: 90px; top: 156px;
    font-family: "Roboto Condensed", "Arial Narrow", sans-serif;
    font-weight: 700;
    font-size: 50px;
    color: var(--signal);
    letter-spacing: 0.2px;
  }
  .services {
    position: absolute;
    right: 90px; top: 314px;
    text-align: right;
  }
  .services__title {
    font-family: "Roboto Condensed", "Arial Narrow", sans-serif;
    font-weight: 700;
    font-size: 34px;
    color: var(--signal);
    line-height: 1.2;
  }
  .services__list {
    list-style: none;
    font-family: "Roboto", Arial, sans-serif;
    font-weight: 400;
    font-size: 28px;
    line-height: 35.5px;
    color: var(--paper);
    margin-top: 2px;
  }
  .contact {
    position: absolute;
    left: 134px; top: 434px;
    list-style: none;
    font-family: "Roboto", Arial, sans-serif;
    font-size: 28px;
    line-height: 35.5px;
    color: var(--paper);
  }
</style>
</head>
<body>
<div class="canvas">
  <svg class="shapes" viewBox="0 0 1196 1458" preserveAspectRatio="none" aria-hidden="true">
    <!-- front card -->
    <rect class="card-front" x="38" y="50" width="1124" height="674" fill="var(--paper)"/>
    <polygon class="front-ridge" fill="var(--ink)" points="38,432 100,462 148,438 180,478 280,486 420,480 465,464 480,400 545,425 578,410 578,365 605,325 640,322 700,330 760,328 800,310 900,315 980,310 1040,293 1100,312 1162,310 1162,724 38,724"/>
    <circle class="mark-dot" cx="470" cy="260" r="62" fill="var(--ink)"/>
    <!-- phone icon -->
    <g class="icon-phone" fill="var(--signal)">
      <path d="M114 540 q16 -10 34 0 l0 6 l-9 0 l0 -4 q-8 -3 -16 0 l0 4 l-9 0 z"/>
      <rect x="119" y="547" width="24" height="15" rx="2"/>
    </g>
    <!-- mail icon -->
    <g class="icon-mail" fill="var(--signal)">
      <polygon points="118,594 134,582 152,594 134,610"/>
    </g>
    <!-- back card -->
    <rect class="card-back" x="38" y="738" width="1124" height="674" fill="var(--signal)"/>
    <polygon class="back-ridge" fill="var(--ink)" points="1100,738 1162,738 1162,1412 385,1412 580,1378 650,1340 860,1320 890,1290 920,1220 975,1215 1045,1135 1010,1100 1040,1045 1050,950 1035,890 1075,825 1065,790"/>
    <circle class="mark-dot" cx="790" cy="1080" r="70" fill="var(--ink)"/>
  </svg>

  <div class="wordmark wordmark--front">Steadfast<br>Vermin<br>Guard</div>

  <div class="holder-name">GAVIN HOLLOWAY</div>

  <div class="services">
    <div class="services__title">SERVICES / INSPECTIONS</div>
    <ul class="services__list">
      <li>Termites, Wood Borers</li>
      <li>Ants, Cockroaches, Spiders</li>
      <li>Fleas, Mice, Rats</li>
      <li>Bed Bugs, &amp; More!</li>
    </ul>
  </div>

  <ul class="contact">
    <li>0461 275 804</li>
    <li>Info@steadfastverminguard.com.au</li>
  </ul>

  <div class="wordmark wordmark--back">Steadfast<br>Vermin<br>Guard</div>
</div>
</body>
</html>
```